A Speech Therapy Business needs to update their logo

I need an update to the font and color of my logo to look more appealing. I am looking to open a private practice as a Speech Language Pathologist that caters to adults and children. It needs to be sophisticated and friendly at the same time. I want to keep the silhouette in my logo as is, just update the font and color for "Brightpaths".
Industry/Entity Type
Business
Contact Information for Business Card
I want the business card to have my logo, my name (Dorota Valk, CCC-SLP, TSSLD) and that I am a Bilingual Speech Language Pathologist. Also, include my phone number, (555) 271-8390. Include my website, Brightpathsslp.example, and email address, dorotavalk@brightpathsslp.example
Look and feel
Each slider illustrates characteristics of the customer's brand and the style your logo design should communicate.

```html
<!DOCTYPE html>
<html lang="en">
<head>
<meta charset="utf-8">
<title>Brightpaths – Business Card</title>
<link rel="stylesheet" href="https://fonts.googleapis.com/css2?family=Barlow:wght@400;500;700&display=swap">
<style>
  :root {
    --backdrop: #e9e6e1;
    --card: #ffffff;
    --card-shade: #eeeeee;
    --brand-blue: #19b0e6;
    --stripe: #1d1d1d;
    --ink: #1e1e1e;
    --silhouette: #2a2a2a;
    --on-blue: #ffffff;
  }
  html, body {
    margin: 0;
    width: 1200px;
    height: 1022px;
    overflow: hidden;
    background: var(--backdrop);
    font-family: "Barlow", "Helvetica Neue", Arial, sans-serif;
  }
  .card {
    position: absolute;
    left: 75px;
    top: 211px;
    width: 1050px;
    height: 600px;
    border-radius: 22px;
    overflow: hidden;
    background: linear-gradient(135deg, var(--card) 0%, var(--card-shade) 100%);
    box-shadow: 0 14px 34px rgba(0,0,0,.18);
  }
  .card__swoosh {
    position: absolute;
    inset: 0;
  }
  .brand {
    position: absolute;
    left: 120px;
    top: 105px;
    width: 360px;
  }
  .brand__silhouettes {
    width: 340px;
    height: 120px;
    background: linear-gradient(90deg, var(--silhouette) 0%, #6a6a6a 100%);
    border-radius: 6px;
  }
  .brand__name {
    margin-top: 18px;
    font-size: 36px;
    font-weight: 500;
    letter-spacing: 10px;
    text-transform: uppercase;
    color: var(--brand-blue);
    white-space: nowrap;
    line-height: 1.1;
  }
  .person {
    position: absolute;
    right: 70px;
    top: 45px;
    text-align: right;
    color: var(--ink);
  }
  .person__name {
    font-size: 46px;
    font-weight: 700;
    letter-spacing: 1px;
    text-transform: uppercase;
    color: var(--brand-blue);
    line-height: 1;
  }
  .person__credentials {
    margin-top: 8px;
    font-size: 29px;
    font-weight: 500;
    letter-spacing: 1px;
    line-height: 1.15;
  }
  .person__role {
    margin-top: 12px;
    font-size: 29px;
    font-weight: 400;
    line-height: 1.15;
    white-space: nowrap;
  }
  .contact {
    position: absolute;
    left: 60px;
    bottom: 40px;
    list-style: none;
    margin: 0;
    padding: 0;
    color: var(--on-blue);
    font-size: 27px;
  }
  .contact__item {
    display: flex;
    align-items: center;
    gap: 16px;
    height: 40px;
  }
  .contact__item--web { font-weight: 700; }
  .contact__icon { width: 20px; height: 20px; flex: none; }
</style>
</head>
<body>
  <section class="card" aria-label="Brightpaths business card">
    <svg class="card__swoosh" viewBox="0 0 1050 600" preserveAspectRatio="none" aria-hidden="true">
      <path d="M0 395 C 330 380, 700 320, 1050 220 L1050 600 L0 600 Z" fill="var(--stripe)"/>
      <path d="M0 418 C 330 403, 700 343, 1050 243 L1050 600 L0 600 Z" fill="var(--card)"/>
      <path d="M0 430 C 330 415, 700 355, 1050 255 L1050 600 L0 600 Z" fill="var(--brand-blue)"/>
    </svg>

    <div class="brand">
      <div class="brand__silhouettes" role="img" aria-label="Silhouette row of figures growing from a toddler to an adult, holding hands"></div>
      <div class="brand__name">Brightpaths</div>
    </div>

    <div class="person">
      <div class="person__name">Dorota Valk</div>
      <div class="person__credentials">CCC-SLP, TSSLD</div>
      <div class="person__role">Bilingual Speech Language Pathologist</div>
    </div>

    <ul class="contact">
      <li class="contact__item">
        <svg class="contact__icon" viewBox="0 0 20 20" aria-hidden="true"><path d="M5 2 L8 6 L6 8 C7 11 9 13 12 14 L14 12 L18 15 L16 18 C9 18 2 11 2 4 Z" fill="none" stroke="currentColor" stroke-width="1.8" stroke-linejoin="round"/></svg>
        (555) 271-8390
      </li>
      <li class="contact__item">
        <svg class="contact__icon" viewBox="0 0 20 20" aria-hidden="true"><rect x="2" y="4" width="16" height="12" fill="none" stroke="currentColor" stroke-width="1.8"/><path d="M2 4 L10 11 L18 4" fill="none" stroke="currentColor" stroke-width="1.8"/></svg>
        dorotavalk@brightpathsslp.example
      </li>
      <li class="contact__item contact__item--web">
        <svg class="contact__icon" viewBox="0 0 20 20" aria-hidden="true"><circle cx="10" cy="10" r="8" fill="none" stroke="currentColor" stroke-width="1.8"/><path d="M2 10 H18 M10 2 C6 6 6 14 10 18 M10 2 C14 6 14 14 10 18" fill="none" stroke="currentColor" stroke-width="1.5"/></svg>
        www.brightpathsslp.example
      </li>
    </ul>
  </section>
</body>
</html>
```